依頼詳細
スパ(ラポルト ミルネ表参道)のお客様向けのDMの作成をお願いいたします。
シンプルで洗練されたデザインでお願いいたします。期間限定の特別トリートメントの訴求です。写真のイメージに合わせたテイストでお願いします。

文字が多いのですが、すっきりと分かりやすくしていただけると幸いです。

本依頼の際に画像の本データは送付いたします。
記載項目
中面:プロモーション内容
宛名面:告知文
希望イメージ
シンプル 複雑
単色 カラフル
暗い 明るい
日常 高級
遊び心 厳粛
未来的 伝統的
女性的 男性的
希望する色
写真に合わせてゴールドを中心に、プラスするなら深いグリーンをでお願いします
納品ファイル
• 高解像度JPG (.jpg)
• イラストレーター形式 (.ai)
補足説明

ブランドのイメージにあったため当選させていただきました。

沢山のご応募ありがとうございました。引き続きどうぞよろしくお願いいたします。

```html
<!DOCTYPE html>
<html lang="ja">
<head>
<meta charset="UTF-8">
<title>シルヴァ ヒーリング スパプログラム</title>
<link rel="stylesheet" href="https://fonts.googleapis.com/css2?family=Noto+Serif+JP:wght@400;500;600;700&family=Noto+Sans+JP:wght@400;500&display=swap">
<style>
  :root {
    --forest: #2e4638;
    --forest-deep: #23372b;
    --gold: #b69a66;
    --gold-soft: #cdb88d;
    --cream: #f3efe8;
    --panel: #ecebe7;
    --ink: #3a3733;
    --ink-soft: #6b6660;
    --white: #ffffff;
  }
  * { margin: 0; padding: 0; box-sizing: border-box; }
  html, body { width: 810px; height: 1200px; overflow: hidden; background: var(--cream); }
  .flyer {
    position: relative;
    width: 810px;
    height: 1200px;
    overflow: hidden;
    font-family: "Noto Serif JP", serif;
    color: var(--ink);
  }
  .hero-photo {
    position: absolute;
    inset: 0 0 270px 0;
    background:
      radial-gradient(ellipse 55% 30% at 40% 62%, #8a5e44 0%, rgba(138,94,68,0) 70%),
      radial-gradient(ellipse 45% 25% at 78% 60%, #d9d2c6 0%, rgba(217,210,198,0) 70%),
      radial-gradient(ellipse 60% 20% at 30% 82%, #5a3c2c 0%, rgba(90,60,44,0) 75%),
      linear-gradient(180deg, #f1eee8 0%, #e9e3da 38%, #b89478 58%, #6e4a37 80%, #4a3226 100%);
  }
  .badges {
    position: absolute;
    top: 40px;
    left: 100px;
    display: flex;
    height: 110px;
  }
  .badge-season {
    width: 170px;
    background: var(--forest);
    color: var(--white);
    display: flex;
    flex-direction: column;
    justify-content: center;
    align-items: center;
    font-size: 30px;
    font-weight: 500;
    line-height: 1.3;
    letter-spacing: 0.04em;
  }
  .badge-start {
    width: 200px;
    background: var(--gold);
    color: var(--white);
    display: flex;
    flex-direction: column;
    justify-content: center;
    align-items: center;
    font-size: 27px;
    font-weight: 500;
    line-height: 1.35;
    white-space: nowrap;
  }
  .badge-start .rule { width: 150px; height: 1px; background: rgba(255,255,255,0.8); margin: 4px 0; }
  .title {
    position: absolute;
    top: 168px;
    left: 100px;
    color: var(--forest-deep);
    font-size: 56px;
    font-weight: 700;
    line-height: 1.2;
    letter-spacing: 0.02em;
    white-space: nowrap;
  }
  .tagline {
    position: absolute;
    top: 792px;
    left: 80px;
    color: var(--white);
    font-size: 31px;
    font-weight: 600;
    line-height: 1.45;
    white-space: nowrap;
    text-shadow: 0 1px 6px rgba(40,25,15,0.55);
  }
  .menu {
    position: absolute;
    left: 0;
    right: 0;
    bottom: 0;
    height: 270px;
    background: var(--panel);
    padding: 18px 70px 0;
  }
  .menu-item { padding: 14px 0 10px; border-bottom: 1px solid var(--gold-soft); }
  .menu-item:last-child { border-bottom: none; }
  .menu-head {
    display: flex;
    justify-content: space-between;
    align-items: baseline;
    gap: 16px;
    font-size: 17px;
    font-weight: 600;
    color: var(--ink);
    white-space: nowrap;
  }
  .menu-name { flex: 1 1 auto; min-width: 0; }
  .menu-price { flex: 0 0 auto; font-weight: 500; }
  .menu-desc {
    margin-top: 6px;
    font-family: "Noto Sans JP", sans-serif;
    font-size: 11px;
    line-height: 1.55;
    color: var(--ink-soft);
  }
</style>
</head>
<body>
<div class="flyer">
  <div class="hero-photo" role="img" aria-label="うつ伏せで施術を受ける女性の背中にキャンドルオイルを垂らす様子と、トリートメントキャンドルの箱とキャンドル"></div>

  <div class="badges">
    <div class="badge-season"><span>2019年</span><span>冬限定</span></div>
    <div class="badge-start"><span>トリートメント</span><span class="rule"></span><span>12/1(日)より</span></div>
  </div>

  <h1 class="title">シルヴァヒーリング<br>スパプログラム</h1>

  <p class="tagline">トリートメントオイルキャンドルで、<br>深い安らぎ、深い森に抱かれて<br>いるような温もりを…</p>

  <section class="menu">
    <div class="menu-item">
      <div class="menu-head"><span class="menu-name">シルヴァ ホットオイル キャンドルトリートメント</span><span class="menu-price">60分／19,800円</span></div>
      <p class="menu-desc">「シルヴァ」とは、北方に広がる針葉樹の森のこと。樹齢を重ねた木々の香りと、キャンドルから溶け出す温かなオイルで、<br>心と体をやさしくほぐし、深い安らぎへと導くボディトリートメントです。</p>
    </div>
    <div class="menu-item">
      <div class="menu-head"><span class="menu-name">シルヴァ ホットストーン キャンドルトリートメント</span><span class="menu-price">90分／26,400円</span></div>
      <p class="menu-desc">キャンドルオイルと温めたストーンで全身をほぐし、巡りを整える極上のリラクゼーショントリートメント。</p>
    </div>
    <div class="menu-item">
      <div class="menu-head"><span class="menu-name">シルヴァ ホットオイル キャンドルトリートメント Premium</span><span class="menu-price">120分／33,000円</span></div>
    </div>
  </section>
</div>
</body>
</html>
```